Ridgefold MMA - Ridgefold Way - 7-5-4

This will be for a wall logo. Probably printed on vinyl to adhere to the wall. This a rough draft concept of the project, but we're certainly open to other designs. Red, Black and White are the main colors we would like to use. The triangle motif is important, it denotes stability and base, which are important in jiu jistu.
The Ridgefold Way (7-5-4)
7 Virtues of a Warrior (Bushido)
R Rectitude
Doing what is right w/o regard for the consequences
C Courage
Inner strength to resist opposition. Courage not just to step on the mat but to make the right decisions
B Benevolence
Mindset to do good. Be kind and generous
P Politeness
Proper consideration and courtesy to others
L Loyalty
Faithfulness & Alliance. Not blind allegiance
H Honesty / Sincerity
Be a man of your word. Do what you say you will
Genuine Integrity in character & action
H Honor
Profound respect & ethical conduct
Make the right decisions to be worthy of respectability
5 Keys to Health
Nutrition - Eat sensibly
Exercise - Stay fit and ready
Rest - Recovery and Recharge
Hygiene - Stay Clean
Attitude - Assume positive intent
Look at life in a positive way
4 States of Mind (Spirit of Budo)
Shoshin - Beginners Mind
Be open to new ideas
Eager to Learn
Zanshin – Remaining Mind
Being Alert and Aware, but relaxed
Be Prepared
Mushin – No Mind (Clear Mind)
Be able to act in the moment without having to think
Fudoshin – Immovable Mind
Emotional Balance
Free from anger, fear, & doubt

```html
<!DOCTYPE html>
<html lang="en">
<head>
<meta charset="utf-8">
<title>The Ridgefold Way (7-5-4)</title>
<link href="https://fonts.googleapis.com/css2?family=Montserrat:wght@800;900&family=Oswald:wght@600;700&family=Nunito:wght@400;500&display=swap" rel="stylesheet">
<style>
:root{
  --red:#b50709;
  --black:#000;
  --charcoal:#2a2a2a;
  --white:#fff;
  --rule:#333;
  --bg-light:#f2f2f2;
  --bg-mid:#dcdcdc;
}
*{margin:0;padding:0;box-sizing:border-box}
html,body{width:848px;height:1200px;overflow:hidden}
body{position:relative;background:var(--bg-light);font-family:"Nunito",sans-serif;color:var(--white)}
.backdrop{position:absolute;inset:0;width:848px;height:1200px}
.abs{position:absolute}
.title{left:0;width:848px;top:40px;text-align:center;font:900 35px/1 "Montserrat",sans-serif;letter-spacing:.5px}
.subtitle{left:0;width:848px;top:125px;text-align:center;font:700 31px/1 "Oswald",sans-serif;letter-spacing:.3px}
.badge{width:50px;height:50px;border-radius:50%;background:var(--red);display:flex;align-items:center;justify-content:center;font:800 26px/1 "Montserrat",sans-serif;transform:translate(-50%,-50%)}
.virtue h3{font:700 24px/1 "Oswald",sans-serif;letter-spacing:.3px;margin-bottom:8px}
.virtue p{font-size:14px;line-height:17px}
.virtue .extra{margin-top:5px}
.right{text-align:right}
.center{text-align:center}
.band-title{font:700 46px/1 "Oswald",sans-serif;top:752px}
.mind h4{font:700 22px/1 "Oswald",sans-serif;margin-bottom:10px}
.mind p{font-size:15px;line-height:19px}
.keys-title{left:24px;width:804px;top:982px;display:grid;grid-template-columns:repeat(14,1fr);text-align:center;font:700 44px/1 "Oswald",sans-serif}
.key svg{width:46px;height:40px;display:block;margin-bottom:16px}
.key h4{font:700 22px/1 "Oswald",sans-serif;margin-bottom:8px}
.key p{font-size:15px;line-height:19px}
</style>
</head>
<body>
<svg class="backdrop" viewBox="0 0 848 1200" aria-hidden="true">
  <defs>
    <linearGradient id="sheen" x1="0" y1="0" x2="1" y2="1">
      <stop offset="0" stop-color="#ececec"/>
      <stop offset=".3" stop-color="#fafafa"/>
      <stop offset=".55" stop-color="#e2e2e2"/>
      <stop offset=".8" stop-color="#f7f7f7"/>
      <stop offset="1" stop-color="#e4e4e4"/>
    </linearGradient>
  </defs>
  <rect width="848" height="724" fill="url(#sheen)"/>
  <polygon points="35.5,23 818,23 772,104.5 82.5,104.5" fill="var(--red)"/>
  <polygon points="35.5,104.5 818,104.5 776,179 77,179" fill="var(--charcoal)"/>
  <rect y="724" width="848" height="240" fill="var(--red)"/>
  <rect y="964" width="848" height="236" fill="var(--black)"/>
  <polygon points="9,179 839,179 424,899" fill="var(--black)"/>
  <g stroke="var(--rule)" stroke-width="1">
    <line x1="166" y1="306" x2="397" y2="306"/>
    <line x1="499" y1="294" x2="729" y2="294"/>
    <line x1="187" y1="439" x2="417" y2="439"/>
    <line x1="466" y1="443" x2="661" y2="443"/>
    <line x1="285" y1="575" x2="564" y2="575"/>
  </g>
  <g stroke="var(--white)" stroke-width="1.5">
    <line x1="207" y1="838" x2="207" y2="946"/>
    <line x1="438" y1="878" x2="438" y2="946"/>
    <line x1="646" y1="838" x2="646" y2="946"/>
  </g>
  <g stroke="var(--red)" stroke-width="1">
    <line x1="169" y1="1066" x2="169" y2="1186"/>
    <line x1="332" y1="1066" x2="332" y2="1186"/>
    <line x1="494" y1="1066" x2="494" y2="1186"/>
    <line x1="661" y1="1066" x2="661" y2="1186"/>
  </g>
</svg>

<h1 class="abs title">THE RIDGEFOLD WAY (7-5-4)</h1>
<h2 class="abs subtitle">7 VIRTUES OF A WARRIOR (BUSHIDO)</h2>

<div class="abs badge" style="left:53px;top:249px">R</div>
<div class="abs badge" style="left:805px;top:240px">P</div>
<div class="abs badge" style="left:112px;top:347px">C</div>
<div class="abs badge" style="left:749px;top:335px">H</div>
<div class="abs badge" style="left:190px;top:492px">B</div>
<div class="abs badge" style="left:663px;top:492px">L</div>
<div class="abs badge" style="left:417.5px;top:793px">H</div>

<div class="abs virtue" style="left:104px;top:217px">
  <h3>RECTITUDE</h3>
  <p>Doing what is right w/o regard<br>for the consequences</p>
</div>
<div class="abs virtue right" style="right:88px;top:208px">
  <h3>POLITENESS</h3>
  <p>Proper consideration and<br>courtesy to others</p>
</div>
<div class="abs virtue" style="left:170px;top:327px">
  <h3>COURAGE</h3>
  <p>Inner strength to resist opposition.<br>Courage not just to step on the mat<br>but to make the right decisions</p>
</div>
<div class="abs virtue right" style="right:151px;top:308px">
  <h3>HONOR</h3>
  <p>Profound respect &amp;<br>ethical conduct</p>
</div>
<div class="abs virtue" style="left:507px;top:388px">
  <p>Make the right decisions to<br>be worthy of respectability</p>
</div>
<div class="abs virtue" style="left:241px;top:470px">
  <h3>BENEVOLENCE</h3>
  <p style="padding-left:3px">Mindset to do good. Be kind<br>and generous</p>
</div>
<div class="abs virtue right" style="right:226px;top:470px">
  <h3 style="margin-right:-7px">LOYALTY</h3>
  <p>Faithfulness &amp; Alliance.<br>Not blind allegiance</p>
</div>
<div class="abs virtue center" style="left:274px;width:300px;top:609px">
  <h3>HONESTY / SINCERITY</h3>
  <p style="margin-top:13px">Be a man of your<br>word. Do what you<br>say you will</p>
  <p class="extra" style="margin-top:10px">Genuine Integrity in<br>character &amp; action</p>
</div>

<h2 class="abs band-title" style="left:31px">4 STATES OF MIND</h2>
<h2 class="abs band-title" style="right:34px">(SPIRIT OF BUDO)</h2>

<div class="abs mind" style="left:31px;top:836px">
  <h4>SHOSHIN</h4>
  <p>Beginners Mind<br>Be open to new ideas<br>Eager to Learn</p>
</div>
<div class="abs mind" style="left:235px;top:836px">
  <h4>ZANSHIN</h4>
  <p>Remaining Mind<br>Being Alert and Aware,<br>but relaxed<br>Be Prepared</p>
</div>
<div class="abs mind" style="left:472px;top:836px">
  <h4>MUSHIN</h4>
  <p>No Mind (Clear Mind)<br>Be able to act in the<br>moment without<br>having to think</p>
</div>
<div class="abs mind" style="left:672px;top:836px">
  <h4>FUDOSHIN</h4>
  <p>Immovable Mind<br>Emotional Balance<br>Free from anger, fear,<br>&amp; doubt</p>
</div>

<h2 class="abs keys-title" aria-label="Keys to Health">
  <span>K</span><span>E</span><span>Y</span><span>S</span><span></span><span>T</span><span>O</span><span></span><span>H</span><span>E</span><span>A</span><span>L</span><span>T</span><span>H</span>
</h2>

<div class="abs key" style="left:34px;top:1054px">
  <svg viewBox="0 0 46 40" fill="none" stroke="var(--red)" stroke-width="2.2" stroke-linecap="round" stroke-linejoin="round"><path d="M14 11c-6-3-12 1-11 9 1 8 6 14 11 12 5 2 9-3 10-9"/><path d="M14 11c2-1 5-1 7 0M14 11c0-3 1-6 3-8"/><path d="M30 10l7 2-6 24c-1 3-5 2-6-1l-2-16c0-5 3-8 7-9z"/><path d="M34 10l3-7M36 11l6-4M27 18h4M26 25h4"/></svg>
  <h4>NUTRITION</h4>
  <p>Eat sensibly</p>
</div>
<div class="abs key" style="left:204px;top:1054px">
  <svg viewBox="0 0 46 40" fill="none" stroke="var(--red)" stroke-width="2.2" stroke-linecap="round" stroke-linejoin="round"><circle cx="10" cy="7" r="4"/><path d="M6 12l4 14 10 0 8 10M20 26l10-8 8 8M10 18l12-4"/><line x1="24" y1="36" x2="44" y2="36"/></svg>
  <h4>EXERCISE</h4>
  <p>&nbsp;Stay fit and<br>ready</p>
</div>
<div class="abs key" style="left:368px;top:1054px">
  <svg viewBox="0 0 46 40" fill="none" stroke="var(--red)" stroke-width="2.2" stroke-linecap="round" stroke-linejoin="round"><circle cx="8" cy="6" r="3.5"/><circle cx="24" cy="8" r="5"/><path d="M24 5v3l2 2"/><path d="M4 14l6 16h14l8 6M10 30l-3 8M22 30l2 8M9 18l12 5"/></svg>
  <h4>REST</h4>
  <p>Recovery and<br>Recharge</p>
</div>
<div class="abs key" style="left:534px;top:1054px">
  <svg viewBox="0 0 46 40" fill="none" stroke="var(--red)" stroke-width="2.2" stroke-linecap="round" stroke-linejoin="round"><path d="M14 22V6a2 2 0 0 1 4 0v12M18 16V3a2 2 0 0 1 4 0v15M22 16V5a2 2 0 0 1 4 0v11M26 16V9a2 2 0 0 1 4 0v10"/><path d="M14 22l-4-5c-2-2-5 0-3 3l6 10c3 5 7 7 12 7"/><path d="M28 22l8 3v6c0 4-4 7-8 8-4-1-8-4-8-8v-6z"/><path d="M24 30l3 3 5-5"/></svg>
  <h4>HYGIENE</h4>
  <p>Stay Clean</p>
</div>
<div class="abs key" style="left:704px;top:1054px">
  <svg viewBox="0 0 46 40" fill="none" stroke="var(--red)" stroke-width="2.2" stroke-linecap="round" stroke-linejoin="round"><path d="M14 38v-8c-4-3-6-7-6-13C8 8 15 2 23 2s14 6 14 15c0 4-2 7-3 9v4h-6v8"/><circle cx="23" cy="16" r="4"/><path d="M23 8v3M23 21v3M15 16h3M28 16h3M17 10l2 2M27 20l2 2M29 10l-2 2M19 20l-2 2"/></svg>
  <h4>ATTITUDE</h4>
  <p>Assume positive<br>intent</p>
</div>
</body>
</html>
```